Floor Inspections and Consulting

We provide inspections and consulting services on various floor coverings, e.g. carpet, hardwood, etc. We also do expert witness work for attorneys due to floor covering failures. We current have a logo, just need it incorporated into a new design. I have examples of cards I have found on the internet that capture my attention and make a statement. I have included our original business card, which in my opinion is terrible, but it does have our logo on it.

```html
<!DOCTYPE html>
<html lang="en">
<head>
<meta charset="utf-8">
<title>Keystone Floor Inspections – Business Card</title>
<link rel="stylesheet" href="https://fonts.googleapis.com/css2?family=Montserrat:wght@700&family=Open+Sans:wght@300;400&display=swap">
<style>
  :root {
    --bg: #e4e4e4;
    --card-white: #f0f0ef;
    --gold: #c3a762;
    --slate: #707174;
    --slate-dark: #4a4b4d;
    --slate-light: #66676a;
    --ink: #5c5c5c;
    --ink-soft: #7a7a7a;
  }
  * { box-sizing: border-box; margin: 0; padding: 0; }
  html, body { width: 1200px; height: 1126px; overflow: hidden; }
  body { background: var(--bg); position: relative; font-family: "Open Sans", sans-serif; }

  .card {
    position: absolute;
    left: 280px;
    width: 640px;
    height: 366px;
    overflow: hidden;
    box-shadow: 0 6px 18px rgba(0,0,0,.18);
  }

  /* Back of card */
  .card-back { top: 165px; background: var(--slate-dark); }
  .card-back .burst {
    position: absolute; inset: 0;
    background: radial-gradient(circle at 50% 50%, var(--slate-light) 0%, #5a5b5e 45%, var(--slate-dark) 100%);
  }
  .card-back .seal {
    position: absolute; left: 50%; top: 50%;
    width: 196px; height: 196px; margin: -98px 0 0 -98px;
    border-radius: 50%; background: var(--card-white);
    display: flex; align-items: center; justify-content: center; text-align: center;
  }
  .card-back .seal-name {
    font-family: "Montserrat", sans-serif; font-weight: 700;
    font-size: 19px; line-height: 1.25; letter-spacing: 1px; color: var(--slate-dark);
  }

  /* Front of card */
  .card-front { top: 595px; background: var(--card-white); }
  .brand-band { position: absolute; left: 96px; top: 0; width: 134px; height: 100%; background: var(--gold); }
  .brand-band .band-cap { position: absolute; left: 0; top: 0; width: 100%; height: 58px; background: var(--slate); }
  .brand-band .seal {
    position: absolute; left: 50%; top: 34px; width: 118px; height: 118px; margin-left: -59px;
    border-radius: 50%; background: var(--card-white);
    display: flex; align-items: center; justify-content: center; text-align: center;
  }
  .brand-band .seal-name {
    font-family: "Montserrat", sans-serif; font-weight: 700;
    font-size: 11.5px; line-height: 1.3; letter-spacing: .5px; color: var(--gold);
  }

  .details { position: absolute; left: 262px; top: 82px; }
  .tagline { font-weight: 300; font-size: 18px; line-height: 1.35; color: var(--ink-soft); }
  .accent-rule { width: 34px; height: 5px; background: var(--gold); margin: 16px 0 36px; }
  .person-name {
    font-family: "Montserrat", sans-serif; font-weight: 700;
    font-size: 25px; letter-spacing: .5px; color: var(--gold); line-height: 1;
  }
  .person-title { font-size: 17px; color: var(--ink); margin-top: 6px; }
  .contact-list { list-style: none; margin-top: 22px; }
  .contact-list li {
    display: flex; align-items: center; gap: 12px;
    font-size: 17px; color: var(--ink); line-height: 1; margin-bottom: 11px;
  }
  .contact-list svg { width: 18px; height: 18px; flex: none; }
</style>
</head>
<body>

<section class="card card-back" aria-label="Card back">
  <div class="burst" role="img" aria-label="Radiating grey sunburst stripes"></div>
  <div class="seal">
    <span class="seal-name">KEYSTONE<br>FLOOR<br>INSPECTIONS</span>
  </div>
</section>

<section class="card card-front" aria-label="Card front">
  <div class="brand-band">
    <div class="band-cap"></div>
    <div class="seal">
      <span class="seal-name">KEYSTONE<br>FLOOR<br>INSPECTIONS</span>
    </div>
  </div>

  <div class="details">
    <p class="tagline">Certified Floor Covering<br>Inspections &amp; Consulting</p>
    <div class="accent-rule"></div>
    <h1 class="person-name">DANIEL MARSH</h1>
    <p class="person-title">President</p>
    <ul class="contact-list">
      <li>
        <svg viewBox="0 0 20 20" aria-hidden="true"><circle cx="10" cy="10" r="10" fill="#c3a762"/><path d="M7 5.5l2 2-1.2 1.3a6 6 0 0 0 3.4 3.4L12.5 11l2 2-1.3 1.5C9.5 14.5 5.5 10.5 5.5 6.8z" fill="#f0f0ef"/></svg>
        555-014-2230
      </li>
      <li>
        <svg viewBox="0 0 20 20" aria-hidden="true"><circle cx="10" cy="10" r="10" fill="#c3a762"/><rect x="5" y="6.5" width="10" height="7" fill="none" stroke="#f0f0ef" stroke-width="1.3"/><path d="M5 6.5l5 4 5-4" fill="none" stroke="#f0f0ef" stroke-width="1.3"/></svg>
        daniel@keystonefloorcheck.com
      </li>
      <li>
        <svg viewBox="0 0 20 20" aria-hidden="true"><circle cx="10" cy="10" r="10" fill="#c3a762"/><g fill="none" stroke="#f0f0ef" stroke-width="1.1"><circle cx="10" cy="10" r="5.5"/><ellipse cx="10" cy="10" rx="2.4" ry="5.5"/><path d="M4.5 10h11M5.5 7h9M5.5 13h9"/></g></svg>
        www.keystonefloorcheck.com
      </li>
    </ul>
  </div>
</section>

</body>
</html>
```